Dermatologist office in Brasilia. My with "target customers" are specially women.

I’m a dermatologist who works since 2006 in Brasilia. In 2017 I decided to change and improve my career. I decided to work more with cosmetics (Veliq and fillers), I still work with clinical and surgical dermatology.
Most of my patients are women but 20-30% are children and men.
I would like to see designs that use a butterfly and the color aquamarine with details in gold.

Industry/Entity Type

Cosmetics

Font styles to use
Sans Serif

Colors
33b8a4
87cfc6
cfeae6
85cae6

Requirements
Must have
• My project must have my name (Harumi Kotaba) and my medical specialty (Dermatologista)
Nice to have
• The colors I prefer are aquamarine or Norwell Blue Box.
• I also prefer a butterfly that means transformation and a new life.
• I prefer a sofisticated and also minimalist design.

```html
<!DOCTYPE html>
<html lang="pt">
<head>
<meta charset="utf-8">
<title>Harumi Kotaba — Dermatologista — Identidade Visual</title>
<link rel="stylesheet" href="https://fonts.googleapis.com/css2?family=Mulish:wght@300;400&display=swap">
<style>
  :root{
    --teal:#2fbcc6;
    --teal-mid:#86cfd6;
    --teal-pale:#d2e9ee;
    --gold:#d9b54a;
    --gold-light:#f3dc86;
    --paper:#ffffff;
    --board:#f6f6f6;
    --shadow:0 2px 4px rgba(0,0,0,.18);
    --font:'Mulish', 'Helvetica Neue', Arial, sans-serif;
  }
  *{box-sizing:border-box;margin:0;padding:0}
  html,body{width:1200px;height:1200px;overflow:hidden}
  body{
    position:relative;
    background:radial-gradient(ellipse at 50% 45%, #ffffff 0%, var(--board) 75%);
    font-family:var(--font);
    color:var(--teal);
  }
  .abs{position:absolute}

  /* Primary lockup */
  .brand-mark{position:absolute;border-radius:50%;background:var(--teal)}
  .brand-mark--gold{background:radial-gradient(circle at 35% 30%, var(--gold-light), var(--gold))}
  .brand-name{font-weight:300;letter-spacing:.2em;white-space:nowrap;color:var(--teal)}
  .brand-role{font-weight:400;letter-spacing:.3em;white-space:nowrap}
  .lockup{left:0;top:0}
  .lockup .brand-mark{left:198px;top:82px;width:64px;height:64px}
  .lockup .brand-name{position:absolute;left:80px;top:178px;font-size:34px}
  .lockup .brand-role{position:absolute;left:147px;top:221px;font-size:13px;color:var(--gold)}

  /* Palette */
  .palette{left:906px;top:96px;display:flex;gap:19px}
  .swatch{width:38px;height:38px;border-radius:50%}
  .swatch--teal{background:var(--teal)}
  .swatch--mid{background:var(--teal-mid)}
  .swatch--pale{background:var(--teal-pale)}
  .swatch--gold{background:radial-gradient(circle at 35% 30%, var(--gold-light), var(--gold))}

  /* Envelopes */
  .envelope{position:absolute;left:68px;width:529px;height:270px;background:var(--teal-pale);box-shadow:var(--shadow)}
  .envelope--back{top:290px}
  .envelope--front{top:593px}
  .envelope__flap{position:absolute;inset:0;width:100%;height:100%}
  .envelope--back .brand-mark{left:102px;top:56px;width:30px;height:30px}
  .envelope--front .brand-name{position:absolute;right:22px;bottom:33px;font-size:14px}
  .envelope--front .brand-role{position:absolute;right:23px;bottom:25px;font-size:5px;color:var(--teal)}

  /* Letterhead */
  .letterhead{left:646px;top:196px;width:470px;height:666px;background:var(--paper);box-shadow:var(--shadow);overflow:hidden}
  .letterhead .brand-mark{left:32px;top:36px;width:36px;height:36px}
  .letterhead .brand-name{position:absolute;left:84px;top:46px;font-size:15px}
  .letterhead .brand-role{position:absolute;left:85px;top:66px;font-size:5px;color:var(--teal)}
  .watermark{position:absolute;border-radius:50%;background:linear-gradient(90deg, rgba(210,233,238,.55), rgba(210,233,238,.15))}
  .letterhead .watermark{left:120px;top:330px;width:360px;height:360px}

  /* Business cards */
  .card{position:absolute;top:943px;width:322px;height:184px;box-shadow:var(--shadow);overflow:hidden}
  .card--front{left:271px;background:var(--teal-pale)}
  .card--front .brand-mark{left:140px;top:50px;width:46px;height:46px}
  .card--front .brand-name{position:absolute;left:0;right:0;top:106px;text-align:center;font-size:19px}
  .card--front .brand-role{position:absolute;left:0;right:0;top:132px;text-align:center;font-size:8px;color:var(--teal)}
  .card--back{left:649px;width:320px;background:var(--paper)}
  .card--back .watermark{left:160px;top:30px;width:150px;height:150px}
  .card--back .brand-role{position:absolute;left:28px;top:34px;font-size:6px;color:var(--teal)}
  .card--back .brand-name{position:absolute;left:28px;top:44px;font-size:14px;letter-spacing:.25em}
  .contact{position:absolute;left:28px;font-size:6.5px;line-height:11px;letter-spacing:.2em;color:var(--teal)}
  .contact--lines{top:83px}
  .contact--address{top:126px}
  .contact span{display:inline-block;width:14px}
</style>
</head>
<body>

  <div class="abs lockup">
    <div class="brand-mark"></div>
    <div class="brand-name">HARUMI KOTABA</div>
    <div class="brand-role">DERMATOLOGISTA</div>
  </div>

  <div class="abs palette">
    <div class="swatch swatch--teal"></div>
    <div class="swatch swatch--mid"></div>
    <div class="swatch swatch--pale"></div>
    <div class="swatch swatch--gold"></div>
  </div>

  <div class="envelope envelope--back">
    <svg class="envelope__flap" viewBox="0 0 529 270" preserveAspectRatio="none">
      <polygon points="0,0 529,0 522,112 7,112" fill="#d6ecf0" stroke="#bcdde3" stroke-width="1"/>
    </svg>
    <div class="brand-mark brand-mark--gold"></div>
  </div>

  <div class="envelope envelope--front">
    <div class="brand-name">HARUMI KOTABA</div>
    <div class="brand-role">DERMATOLOGISTA</div>
  </div>

  <div class="abs letterhead">
    <div class="watermark" role="img" aria-label="Faint decorative area"></div>
    <div class="brand-mark"></div>
    <div class="brand-name">HARUMI KOTABA</div>
    <div class="brand-role">DERMATOLOGISTA</div>
  </div>

  <div class="card card--front">
    <div class="brand-mark brand-mark--gold"></div>
    <div class="brand-name">HARUMI KOTABA</div>
    <div class="brand-role">DERMATOLOGISTA</div>
  </div>

  <div class="card card--back">
    <div class="watermark" role="img" aria-label="Faint decorative area"></div>
    <div class="brand-role">DERMATOLOGISTA</div>
    <div class="brand-name">HARUMI KOTABA</div>
    <div class="contact contact--lines">
      <span>E</span>info@harumikotaba.com<br>
      <span>T</span>+55 0987 654321<br>
      <span>F</span>+55 0987 654320
    </div>
    <div class="contact contact--address">
      1 Abcde Street,<br>
      Fghijk, Lmnop,<br>
      Qrstuv, 00000, Brazil
    </div>
  </div>

</body>
</html>
```